Powepoint template for an investment group

Need high end clear clean concise creative luxurious

Have royal clients
High end/billionaire investors

Using ross gold logo can be creative
Must habe page numbers
Logo preference header top right
Page number footer bottom right

The first page of the ppt maybe a big block of dark grey and ulvo investment group written on the front page in rose gold

Target Market(s)

Investors at a high level

Requirements
Must have
• Luxury feel

```html
<!DOCTYPE html>
<html lang="en">
<head>
<meta charset="utf-8">
<title>Ulvo Investment Group – Presentation Template</title>
<link rel="stylesheet" href="https://fonts.googleapis.com/css2?family=Josefin+Sans:wght@200;300&family=Roboto:wght@300;400;700&display=swap">
<style>
:root{
  --page:#ffffff;
  --slide:#1a1819;
  --rose:#c9907d;
  --rose-light:#dba694;
  --text:#e6e1df;
  --muted:#cfc9c7;
  --rule:#8c8683;
}
*{box-sizing:border-box;margin:0;padding:0}
html,body{width:1200px;height:3797px;overflow:hidden;background:var(--page)}
body{position:relative;font-family:'Roboto',Arial,sans-serif;color:var(--text)}
.slide{position:absolute;left:108px;width:981px;height:552px;background:var(--slide);overflow:hidden}
.slide-title{position:absolute;top:24px;font-size:21px;font-weight:400;letter-spacing:1.5px;color:var(--rose-light)}
.brand{position:absolute;top:12px;right:12px;width:110px;text-align:center;color:var(--rose);font-family:'Josefin Sans',sans-serif;font-weight:200;line-height:1}
.brand-name{display:block;font-size:30px;letter-spacing:8px;margin-right:-8px}
.brand-sub{display:block;font-size:8px;letter-spacing:1px;margin-top:4px}
.page-no{position:absolute;right:2px;bottom:-2px;width:24px;height:24px;border-radius:50%;background:var(--rose);color:#3a2823;font-size:9px;text-align:center;line-height:20px}
.photo{position:absolute}
.hero{display:flex;flex-direction:column;align-items:center;color:var(--rose);font-family:'Josefin Sans',sans-serif;font-weight:200}
.hero-name{position:absolute;left:0;right:0;text-align:center;font-size:118px;letter-spacing:42px;text-indent:42px;line-height:1}
.hero-sub{position:absolute;left:0;right:0;text-align:center;font-size:33px;letter-spacing:3px}
.about-heading{position:absolute;left:564px;top:140px;width:340px;font-size:23px;font-weight:400;line-height:28px;letter-spacing:.5px;color:#fff}
.about-copy{position:absolute;left:568px;top:246px;width:335px;font-size:15px;font-weight:300;line-height:21.6px;color:var(--muted)}
.service{position:absolute;left:29px;width:400px}
.service-icon{position:absolute;left:0;width:72px;height:72px;border-radius:50%;background:var(--rose);display:flex;align-items:center;justify-content:center}
.service-body{position:absolute;left:98px;width:275px}
.item-heading{font-size:12.5px;font-weight:700;letter-spacing:.3px;color:#fff}
.item-copy{margin-top:12px;font-size:12.3px;font-weight:300;line-height:16.4px;color:var(--muted)}
.solution{position:absolute;top:93px;width:287px}
.solution .photo{position:relative;width:287px;height:197px;display:block}
.solution .item-heading{margin-top:33px}
.solution .item-copy{margin-top:13px;font-size:12px;line-height:16.4px}
.invest-block{position:absolute;left:56px;width:410px}
.invest-heading{font-size:18px;font-weight:400;line-height:23px;letter-spacing:.3px;color:#fff}
.invest-copy{margin-top:18px;font-size:14px;font-weight:300;line-height:18px;color:var(--muted)}
.thanks{position:absolute;left:370px;width:241px;top:319px;height:75px;border-top:1.5px solid var(--rule);border-bottom:1.5px solid var(--rule);display:flex;align-items:center;justify-content:center;font-size:35px;letter-spacing:2px;color:#fff;font-weight:400}
</style>
</head>
<body>

<!-- Cover -->
<section class="slide" style="top:79px">
  <div class="hero">
    <span class="hero-name" style="top:188px">ULVO</span>
    <span class="hero-sub" style="top:310px">Investment Group</span>
  </div>
</section>

<!-- About us -->
<section class="slide" style="top:680px">
  <h2 class="slide-title" style="left:26px">ABOUT US</h2>
  <div class="brand"><span class="brand-name">ULVO</span><span class="brand-sub">Investment Group</span></div>
  <div class="photo" role="img" aria-label="Team reviewing financial charts and a tablet on a desk" style="left:25px;top:85px;width:492px;height:432px;background:linear-gradient(135deg,#2b3a4a 0%,#6b7c8c 40%,#d9d4cc 75%,#b98f6c 100%)"></div>
  <h3 class="about-heading">LOREM IPSUM IS SIMPLY DUMMY TEXT OF THE PRIN TING AND TYPESETTING</h3>
  <p class="about-copy">There are many variations of passages of Lorem Ipsum available, but the majority have suffered alteration in some form, by injected humour, or randomised words which don't look even slightly believable. If you are going to use a passage of Lorem Ipsum, you need to be sure there isn't anything embarrassing hidden in the middle of text. All the Lorem Ipsum generators on the Internet tend to repeat predefined</p>
  <span class="page-no">01</span>
</section>

<!-- Services -->
<section class="slide" style="top:1281px">
  <h2 class="slide-title" style="left:35px">SERVICES</h2>
  <div class="brand"><span class="brand-name">ULVO</span><span class="brand-sub">Investment Group</span></div>

  <div class="service" style="top:122px">
    <div class="service-icon" style="top:0">
      <svg width="36" height="36" viewBox="0 0 36 36" fill="#1a1819"><circle cx="11" cy="9" r="5"/><path d="M2 27c0-6 4-10 9-10s9 4 9 10z"/><rect x="22" y="22" width="3" height="8"/><rect x="27" y="17" width="3" height="13"/><rect x="32" y="12" width="3" height="18"/><text x="24" y="12" font-size="12" font-weight="700" font-family="Roboto,sans-serif">$</text></svg>
    </div>
    <div class="service-body" style="top:-3px"><h4 class="item-heading">LOREM IPSUM IS SIMPLY DUMMY</h4><p class="item-copy">There are many variations of passages of Lorem Ipsum available, but the majority have suffered alteration in some form, by injected humour, or randomised words which</p></div>
  </div>
  <div class="service" style="top:269px">
    <div class="service-icon" style="top:0">
      <svg width="34" height="34" viewBox="0 0 34 34" fill="none" stroke="#1a1819" stroke-width="3.5"><path d="M15 6H6v22h22v-9"/><path d="M26 4l4 4-13 13h-4v-4z" fill="#1a1819"/></svg>
    </div>
    <div class="service-body" style="top:-3px"><h4 class="item-heading">LOREM IPSUM IS SIMPLY DUMMY</h4><p class="item-copy">There are many variations of passages of Lorem Ipsum available, but the majority have suffered alteration in some form, by injected humour, or randomised words which</p></div>
  </div>
  <div class="service" style="top:416px">
    <div class="service-icon" style="top:0">
      <svg width="38" height="38" viewBox="0 0 24 24" fill="#1a1819"><path d="M19.4 13a7.5 7.5 0 000-2l2.1-1.6-2-3.5-2.5 1a7.6 7.6 0 00-1.7-1L15 3h-4l-.4 2.7a7.6 7.6 0 00-1.7 1l-2.5-1-2 3.5L6.5 11a7.5 7.5 0 000 2l-2.1 1.6 2 3.5 2.5-1a7.6 7.6 0 001.7 1L11 21h4l.4-2.7a7.6 7.6 0 001.7-1l2.5 1 2-3.5zM13 15.5a3.5 3.5 0 110-7 3.5 3.5 0 010 7z" transform="translate(-1 0)"/></svg>
    </div>
    <div class="service-body" style="top:-3px"><h4 class="item-heading">LOREM IPSUM IS SIMPLY DUMMY</h4><p class="item-copy">There are many variations of passages of Lorem Ipsum available, but the majority have suffered alteration in some form, by injected humour, or randomised words which</p></div>
  </div>

  <div class="photo" role="img" aria-label="Hand placing coins beside a glowing stock chart graphic" style="left:453px;top:90px;width:493px;height:434px;background:linear-gradient(160deg,#5e7a8a 0%,#8fb1bf 45%,#cfe3e8 75%,#a9c6cf 100%)"></div>
  <span class="page-no">02</span>
</section>

<!-- Solutions -->
<section class="slide" style="top:1881px">
  <h2 class="slide-title" style="left:24px">SOLUTIONS</h2>
  <div class="brand"><span class="brand-name">ULVO</span><span class="brand-sub">Investment Group</span></div>

  <div class="solution" style="left:23px">
    <div class="photo" role="img" aria-label="Businessman touching a hexagon interface labelled invest" style="background:linear-gradient(135deg,#3a4d6b 0%,#7d93b5 50%,#2f5fb8 80%,#22304a 100%)"></div>
    <h4 class="item-heading">LOREM IPSUM IS SIMPLY DUMMY</h4>
    <p class="item-copy">It is a long established fact that a reader will be distracted by the readable content of a page when looking at its layout. The point of using Lorem Ipsum is that it has a more-or-less normal distribution of letters, as opposed to using 'Content here, content here', making it look like readable English. Many desktop publishing packages and web page editors now use Lorem Ipsum as their default model text, and a search for 'lorem ipsum' will uncover many web sites still in their infancy</p>
  </div>
  <div class="solution" style="left:346px">
    <div class="photo" role="img" aria-label="Hands holding a tablet with a glowing bar chart" style="background:linear-gradient(135deg,#0e0f14 0%,#2a2b36 45%,#8a5a7a 70%,#151620 100%)"></div>
    <h4 class="item-heading">LOREM IPSUM IS SIMPLY DUMMY</h4>
    <p class="item-copy">It is a long established fact that a reader will be distracted by the readable content of a page when looking at its layout. The point of using Lorem Ipsum is that it has a more-or-less normal distribution of letters, as opposed to using 'Content here, content here', making it look like readable English. Many desktop publishing packages and web page editors now use Lorem Ipsum as their default model text, and a search for 'lorem ipsum' will uncover many web sites still in their infancy</p>
  </div>
  <div class="solution" style="left:668px">
    <div class="photo" role="img" aria-label="Businessman working on a laptop in a modern office" style="background:linear-gradient(135deg,#1c2a38 0%,#4b6070 45%,#a9b3b8 70%,#2a3a48 100%)"></div>
    <h4 class="item-heading">LOREM IPSUM IS SIMPLY DUMMY</h4>
    <p class="item-copy">It is a long established fact that a reader will be distracted by the readable content of a page when looking at its layout. The point of using Lorem Ipsum is that it has a more-or-less normal distribution of letters, as opposed to using 'Content here, content here', making it look like readable English. Many desktop publishing packages and web page editors now use Lorem Ipsum as their default model text, and a search for 'lorem ipsum' will uncover many web sites still in their infancy</p>
  </div>
  <span class="page-no">03</span>
</section>

<!-- Investment -->
<section class="slide" style="top:2482px">
  <h2 class="slide-title" style="left:29px">INVESTMENT</h2>
  <div class="brand"><span class="brand-name">ULVO</span><span class="brand-sub">Investment Group</span></div>

  <div class="invest-block" style="top:90px">
    <h3 class="invest-heading">LOREM IPSUM IS SIMPLY DUMMY<br>TEXT OF THE PRIN TING</h3>
    <p class="invest-copy">There are many variations of passages of Lorem Ipsum available, but the majority have suffered alteration in some form, by injected humour, or randomised words which don't look even slightly believable. If you are going to use a passage of Lorem Ipsum, you need to be sure there isn't anything embarrassing hidden in the middle of text.</p>
  </div>
  <div class="invest-block" style="top:299px">
    <h3 class="invest-heading">LOREM IPSUM IS SIMPLY DUMMY<br>TEXT OF THE PRIN TING</h3>
    <p class="invest-copy">There are many variations of passages of Lorem Ipsum available, but the majority have suffered alteration in some form, by injected humour, or randomised words which don't look even slightly believable. If you are going to use a passage of Lorem Ipsum, you need to be sure there isn't anything embarrassing hidden in the middle of text.</p>
  </div>

  <svg class="photo" style="left:0;top:0" width="981" height="552" viewBox="0 0 981 552">
    <defs>
      <linearGradient id="invest-main" x1="0" y1="0" x2="1" y2="1"><stop offset="0" stop-color="#4a4340"/><stop offset=".45" stop-color="#8a6f62"/><stop offset=".8" stop-color="#1f3f6b"/><stop offset="1" stop-color="#12264a"/></linearGradient>
      <linearGradient id="invest-a" x1="0" y1="0" x2="1" y2="1"><stop offset="0" stop-color="#d8d6d2"/><stop offset="1" stop-color="#5a5450"/></linearGradient>
      <linearGradient id="invest-b" x1="0" y1="0" x2="1" y2="1"><stop offset="0" stop-color="#3e4f56"/><stop offset="1" stop-color="#9aa6a8"/></linearGradient>
      <linearGradient id="invest-c" x1="0" y1="0" x2="1" y2="1"><stop offset="0" stop-color="#0b1e46"/><stop offset="1" stop-color="#2f6fc4"/></linearGradient>
    </defs>
    <polygon role="img" aria-label="Businessman studying data with a blue digital overlay" points="541,63 981,63 981,552 848,552" fill="url(#invest-main)"/>
    <circle role="img" aria-label="Two colleagues meeting in a bright office" cx="592" cy="121" r="84" fill="url(#invest-a)" stroke="#1a1819" stroke-width="3"/>
    <circle role="img" aria-label="Businessman holding a laptop" cx="689" cy="253" r="69" fill="url(#invest-b)" stroke="#1a1819" stroke-width="3"/>
    <circle role="img" aria-label="Hand touching a glowing digital globe" cx="782" cy="372" r="65" fill="url(#invest-c)" stroke="#1a1819" stroke-width="3"/>
  </svg>
  <span class="page-no">04</span>
</section>

<!-- Closing -->
<section class="slide" style="top:3084px">
  <div class="hero">
    <span class="hero-name" style="top:112px">ULVO</span>
    <span class="hero-sub" style="top:226px">Investment Group</span>
  </div>
  <div class="thanks">THANK YOU</div>
</section>

</body>
</html>
```